Kestrel Dental personal information forms

We are a Dental Practice that require an update to our information forms, there are 3 versions of it.
I will attach our old ones, we need to keep the same information on there, we just want them to look better and use our current logo and colours.
Our website is www.kestreldental.net
Our facebook is www.friendnook.com/kestreldentalbrookplaza/
..................................................................................................

Target Market(s)

Everyone, easy to read

Industry/Entity Type

Dental Clinic

Colors
0692cd
34a6d7
cee9f5
ffffff
0255a3
3276b5

Requirements
Must have
• Logo
• Our colours
• same information as the uploaded versions
Should not have
• any other colour besides the blues, black and white

```html
<!DOCTYPE html>
<html lang="en">
<head>
<meta charset="utf-8">
<title>Kestrel Dental – Patient Information Update</title>
<link href="https://fonts.googleapis.com/css2?family=Source+Sans+3:ital,wght@0,400;0,600;0,700;1,600;1,700;1,800&display=swap" rel="stylesheet">
<style>
:root{
  --backdrop:#8e8f93;
  --paper:#ffffff;
  --ink:#1a1a1a;
  --brand:#0692cd;
  --brand-deep:#0255a3;
  --brand-mid:#3276b5;
  --brand-soft:#34a6d7;
  --fill-pale:#cee9f5;
}
*{box-sizing:border-box;margin:0;padding:0}
html,body{width:960px;height:1200px;overflow:hidden}
body{background:var(--backdrop);font-family:"Source Sans 3",Arial,sans-serif;color:var(--ink);position:relative}
.abs{position:absolute}
.sheet{left:49px;top:52px;width:859px;height:1110px;background:var(--paper)}
.top-rule{left:49px;top:52px;width:859px;height:7px;background:var(--brand-mid)}
.hero-photo{left:49px;top:59px;width:859px;height:106px;background:linear-gradient(180deg,#e4ecf4 0%,#f1f5f9 55%,#ffffff 100%)}
.logo-banner{left:343px;top:59px}
.practice-name{left:343px;top:75px;width:273px;text-align:center;color:#fff;font-weight:600;font-size:28px;line-height:36px}
.doctors{left:109px;top:167px;font-size:13.5px;line-height:17px}
.welcome{left:560px;top:172px;width:336px;text-align:right;font-weight:800;font-style:italic;font-size:19px}
.intro{left:95px;top:212px;width:772px;font-size:14.6px;line-height:20.5px}
.form-frame{left:94px;top:308px;width:770px;height:816px;border:1.5px solid var(--brand-mid)}
.form-band{left:94px;top:308px;width:770px;height:17px;background:var(--brand-mid)}
.band-title{top:308px;color:#fff;font-size:13px;line-height:17px;text-align:center}
.box{display:inline-block;width:9px;height:9px;border:1px solid #333;margin-right:4px;vertical-align:-1px;background:#fff}
.titles{left:112px;top:334px;font-size:13px;word-spacing:2px}
.titles span.opt{margin-right:9px}
.table{border:1px solid var(--brand-mid);border-bottom:none;font-size:13px}
.row{display:flex;border-bottom:1px solid var(--brand-mid);height:20px}
.row .label{border-right:1px solid var(--brand-mid);padding:0 0 0 6px;line-height:19px}
.row .field{flex:1;position:relative;padding-left:3px;line-height:19px}
.row .split{border-left:1px solid var(--brand-mid);width:140px;padding-left:4px;line-height:19px}
.block{display:flex;border-bottom:1px solid var(--brand-mid)}
.block .label{border-right:1px solid var(--brand-mid);padding:0 0 0 6px;line-height:20px}
.block .fields{flex:1}
.block .fields .row:last-child{border-bottom:none}
.patient{left:112px;top:358px;width:417px}
.patient .label{width:123px}
.contact{left:546px;top:358px;width:291px}
.contact .label{width:87px}
.full{padding-left:6px;line-height:19px;flex:1}
.emergency-head{left:546px;top:517px;width:291px;height:21px;background:var(--brand-mid);color:#fff;text-align:center;font-size:13px;line-height:21px}
.emergency{left:546px;top:538px;width:291px}
.emergency .label{width:87px}
.q{left:112px;font-size:12.4px;font-weight:600;line-height:14px}
.yn{font-size:12px;font-weight:600}
.answer-bar{left:112px;width:739px;height:19px;background:var(--fill-pale)}
.conditions{left:137px;top:746px;font-size:12px;font-weight:600;line-height:14px;list-style:none}
.declare{left:112px;top:991px;width:742px;font-size:12px;font-weight:700;font-style:italic;line-height:15px}
.legal{left:112px;top:1024px;width:742px;font-size:11px;line-height:14px}
.sign{top:1092px;font-size:12px;font-weight:600}
.sign-line{top:1105px;height:1.5px;background:var(--brand-mid)}
.site{left:49px;top:1131px;width:859px;text-align:center;font-size:14px;letter-spacing:4.5px;font-weight:600;color:#333}
</style>
</head>
<body>
<div class="abs sheet"></div>
<div class="abs hero-photo" role="img" aria-label="Soft photo of dental instruments and model teeth across the header"></div>
<div class="abs top-rule"></div>
<svg class="abs logo-banner" width="273" height="68" viewBox="0 0 273 68" aria-hidden="true">
  <polygon points="0,0 273,0 273,44 249,68 24,68 0,44" fill="var(--brand)"/>
</svg>
<div class="abs practice-name">Kestrel Dental</div>

<div class="abs doctors">Dr. Peter Holloway &amp; Dr. Simon Ashdown<br>Dental Surgeons</div>
<div class="abs welcome">Welcome back to our practive!</div>
<p class="abs intro">THIS INFORMATION IS CONFIDENTIAL and is necessary to enable us to offer you THE BEST POSSIBLE CARE. Because we haven’t seen you in some time and because we care about your health staus, please take you time and thoroughly complete the following update of your personal and medical information it is essential that we know about your past and present medical history. Many medical conditions my interfere with dental procedures.</p>

<div class="abs form-frame"></div>
<div class="abs form-band"></div>
<div class="abs band-title" style="left:168px;width:260px">PATIENT INFORMATION</div>
<div class="abs band-title" style="left:580px;width:290px">PATIENT CONTACT INFORMATION</div>

<div class="abs titles">
  <span class="opt"><span class="box"></span>Ms</span>
  <span class="opt"><span class="box"></span>Mrs</span>
  <span class="opt"><span class="box"></span>Miss</span>
  <span class="opt"><span class="box"></span>Mr</span>
  <span class="opt"><span class="box"></span>Master</span>
  <span class="opt"><span class="box"></span>Dr</span>
  <span class="opt"><span class="box"></span>Other</span>
</div>

<div class="abs table patient">
  <div class="row"><div class="label">Surname</div><div class="field"></div></div>
  <div class="row"><div class="label">First Name</div><div class="field"></div></div>
  <div class="row"><div class="label">Prefered</div><div class="field"></div></div>
  <div class="row"><div class="label">Date of Birth</div><div class="field"></div></div>
  <div class="block">
    <div class="label">Current<br>Residential<br>Address</div>
    <div class="fields">
      <div class="row"><div class="field"></div></div>
      <div class="row"><div class="field"></div></div>
      <div class="row"><div class="field"></div><div class="split">Postcode:</div></div>
    </div>
  </div>
  <div class="block">
    <div class="label">Postal<br>Residential<br>Address<br>(if different)</div>
    <div class="fields">
      <div class="row"><div class="field"></div></div>
      <div class="row"><div class="field"></div></div>
      <div class="row"><div class="field"></div></div>
      <div class="row"><div class="field"></div><div class="split">Postcode:</div></div>
    </div>
  </div>
  <div class="row"><div class="label">Occupation</div><div class="field"></div></div>
  <div class="row"><div class="label">Employer</div><div class="field"></div></div>
</div>

<div class="abs table contact">
  <div class="block">
    <div class="label">Phone</div>
    <div class="fields">
      <div class="row"><div class="field">M:</div></div>
      <div class="row"><div class="field">H:</div></div>
      <div class="row"><div class="field">W:</div></div>
    </div>
  </div>
  <div class="row"><div class="label">Email</div><div class="field"></div></div>
  <div class="row"><div class="label">Prefered</div><div class="field"></div></div>
  <div class="row"><div class="full">Prefered Method of communication</div></div>
  <div class="row"><div class="full"><span class="box"></span>SMS &nbsp;<span class="box"></span>Phone &nbsp;<span class="box"></span>Email &nbsp;<span class="box"></span>Mail</div></div>
</div>

<div class="abs emergency-head">EMERGENCY CONTACT</div>
<div class="abs table emergency">
  <div class="row"><div class="label">Name</div><div class="field"></div></div>
  <div class="row"><div class="label">Relation</div><div class="field"></div></div>
  <div class="row" style="height:42px"><div class="label" style="line-height:20px">Contact<br>Number</div><div class="field"></div></div>
</div>

<div class="abs q" style="top:639px">Are you currently or have you taken any prescribed medication or dietary supplements in the last 12 months?<br>(If YES, Please list below)</div>
<div class="abs yn" style="left:776px;top:640px"><span class="box"></span>YES</div>
<div class="abs yn" style="left:819px;top:640px"><span class="box"></span>NO</div>
<div class="abs answer-bar" style="top:669px"></div>

<div class="abs q" style="top:690px">Allegies / Reactions? (If YES, Please list below)</div>
<div class="abs yn" style="left:776px;top:689px"><span class="box"></span>YES</div>
<div class="abs yn" style="left:819px;top:689px"><span class="box"></span>NO</div>
<div class="abs answer-bar" style="top:709px"></div>

<div class="abs q" style="top:728px">Have you ever has or are your suffering from any of the following? please tick any that apply:</div>
<ul class="abs conditions">
  <li><span class="box"></span>Rheumatic fever</li>
  <li><span class="box"></span>Epilepsy</li>
  <li><span class="box"></span>Asthma</li>
  <li><span class="box"></span>Tuberculosis</li>
  <li><span class="box"></span>Radiation Therapy</li>
  <li><span class="box"></span>Sizziness, fainting</li>
  <li><span class="box"></span>Hepatitis A B or C</li>
  <li><span class="box"></span>Recent eye surgery</li>
</ul>
<ul class="abs conditions" style="left:358px">
  <li><span class="box"></span>Diabetes</li>
  <li><span class="box"></span>Kidney Disease</li>
  <li><span class="box"></span>Heart Attack</li>
  <li><span class="box"></span>High Blood Pressure</li>
  <li><span class="box"></span>Bleeding problems</li>
  <li><span class="box"></span>Artificial joints</li>
  <li><span class="box"></span>Respiratory problems</li>
</ul>
<ul class="abs conditions" style="left:574px">
  <li><span class="box"></span>HIVE positive</li>
  <li><span class="box"></span>High cholesterol</li>
  <li><span class="box"></span>Cancer</li>
  <li><span class="box"></span>Pace-maker</li>
  <li><span class="box"></span>Osteoporosis</li>
  <li><span class="box"></span>Heat rate problems</li>
  <li><span class="box"></span>Heart murmur</li>
</ul>

<div class="abs q" style="top:868px">Do you have any disease, or condition or problem not listed above?</div>
<div class="abs yn" style="left:776px;top:866px"><span class="box"></span>YES</div>
<div class="abs yn" style="left:819px;top:866px"><span class="box"></span>NO</div>
<div class="abs answer-bar" style="top:884px"></div>

<div class="abs q" style="top:909px">Have you had surgery or been to hospital in the last 5 years? |(if YES, please give details)</div>
<div class="abs yn" style="left:776px;top:907px"><span class="box"></span>YES</div>
<div class="abs yn" style="left:819px;top:907px"><span class="box"></span>NO</div>
<div class="abs answer-bar" style="top:926px"></div>

<div class="abs q" style="top:949px">For Women: Are you pregnant? If YES, how many months?</div>
<div class="abs yn" style="left:776px;top:947px"><span class="box"></span>YES</div>
<div class="abs yn" style="left:819px;top:947px"><span class="box"></span>NO</div>
<div class="abs answer-bar" style="top:967px"></div>

<p class="abs declare">The information that I provided is to the best of my knowledge tru and current and I understand that it is my responsibility to inform of any changes in my medical status.</p>
<p class="abs legal">This is to certify that I, the undersigned, consent to the performing of the dental and oral surgery procedure agreed to be necessary or advisable, include the use of local anaesthetic as indicated and I will assume responsibility &nbsp;for the fees associated with these procedures. Therefore, I shall pay any legal cost, including solicitor own costs, tracing costs and may collection commission incurred by Kestrel Dental as a result of my failure to pay any amount due to Kestrel Dental.</p>

<div class="abs sign" style="left:112px">Patient/Parent/Person Responsible Signature:</div>
<div class="abs sign-line" style="left:372px;width:212px"></div>
<div class="abs sign" style="left:609px">Date:</div>
<div class="abs sign-line" style="left:648px;width:203px"></div>

<div class="abs site">www.kestreldental.net</div>
</body>
</html>
```